Tallow Crest Software PowerPoint template

We are a software company selling endpoint visibility, access and security technology to enterprise-level IT departments.
Our technology helps organizations gain comprehensive visibility into and control over devices accessing their corporate network so they can quickly identify and address suspicious activity on the network that could lead to potential threats like data breaches.
This technology can cost organizations upwards of $1M - depending on the size of the organization. Our primary clients are Meridane 2,000 companies.
We want a professional, polished PowerPoint template that we can use for all company presentations. Please include:
Title page
Section page
General info page
Thank you page
Logo options and color specs are attached.
Please include our tagline on at least the title page: Discover the edge. Optimize the whole.

```html
<!DOCTYPE html>
<html lang="en">
<head>
<meta charset="utf-8">
<title>Tallow Crest Software – About Us</title>
<link rel="stylesheet" href="https://fonts.googleapis.com/css2?family=Carlito:wght@400;700&family=Raleway:wght@500;700&display=swap">
<style>
  :root {
    --brand-red: #8e1b1f;
    --brand-orange: #d3825f;
    --ink: #1a1a1a;
    --muted: #555555;
    --rule: #b9b9b9;
    --paper: #ffffff;
    --pattern-tone: #eeeeee;
  }
  * { box-sizing: border-box; margin: 0; padding: 0; }
  html, body { width: 1200px; height: 849px; overflow: hidden; background: var(--paper); }
  .slide {
    position: relative;
    width: 1200px;
    height: 849px;
    background: var(--paper);
    font-family: "Carlito", "Calibri", sans-serif;
    color: var(--ink);
    overflow: hidden;
  }
  .header-bar {
    position: absolute; left: 134px; top: 0;
    width: 6px; height: 86px;
    background: var(--brand-red);
  }
  .header-title {
    position: absolute; left: 161px; top: 36px;
    font-family: "Raleway", sans-serif; font-weight: 500;
    font-size: 20px; color: var(--brand-red); letter-spacing: 0.2px;
  }
  .header-date {
    position: absolute; left: 161px; top: 61px;
    font-family: "Raleway", sans-serif; font-weight: 500;
    font-size: 19px; color: var(--ink);
  }
  .header-date strong { font-weight: 700; }
  .pattern-area {
    position: absolute; right: 0; top: 0;
    width: 372px; height: 360px;
    background: radial-gradient(ellipse at 75% 30%, var(--pattern-tone) 0%, rgba(238,238,238,0.4) 45%, rgba(255,255,255,0) 75%);
  }
  .page-number {
    position: absolute; left: 1098px; top: 36px;
    width: 56px; height: 56px; border-radius: 50%;
    background: var(--brand-orange); color: var(--paper);
    font-family: "Raleway", sans-serif; font-weight: 700; font-size: 16px;
    display: flex; align-items: center; justify-content: center;
  }
  .page-title {
    position: absolute; left: 128px; top: 168px;
    font-family: "Raleway", sans-serif; font-weight: 700;
    font-size: 70px; line-height: 1; color: var(--brand-orange);
  }
  .body-copy {
    position: absolute; left: 125px; top: 284px;
    width: 880px;
    font-size: 15.6px; line-height: 24.6px; color: var(--ink);
  }
  .body-copy p + p { margin-top: 7px; }
  .footer-rule {
    position: absolute; left: 131px; top: 770px;
    width: 705px; height: 1px; background: var(--rule);
  }
  .footer-copyright {
    position: absolute; left: 133px; top: 779px;
    font-size: 12px; color: var(--muted);
  }
  .footer-brand {
    position: absolute; left: 852px; top: 748px;
    display: flex; align-items: center; gap: 14px;
  }
  .brand-dot {
    width: 44px; height: 44px; border-radius: 50%;
    background: var(--brand-orange);
  }
  .brand-name {
    font-family: "Raleway", sans-serif; font-weight: 700;
    font-size: 22px; letter-spacing: 2px; color: var(--brand-red);
    text-transform: uppercase; line-height: 1.1;
  }
</style>
</head>
<body>
  <main class="slide">
    <div class="header-bar"></div>
    <div class="header-title">PPT HEADING GOES HERE</div>
    <div class="header-date">FEB, <strong>2015</strong></div>

    <div class="pattern-area" role="img" aria-label="Decorative pattern of outlined circles"></div>
    <div class="page-number">01</div>

    <h1 class="page-title">About Us</h1>

    <section class="body-copy">
      <p>Our technology helps organizations gain comprehensive visibility into and control over devices accessing their corporate network so they can quickly identify and address suspicious activity on the network that could lead to potential threats like data breaches. Our technology helps organizations gain comprehensive visibility into and control over devices accessing their corporate network so they can quickly identify and address suspicious activity on the network that could lead to potential threats like data breaches. Our technology helps organizations gain comprehensive visibility into and control over devices accessing their corporate network so they can quickly identify and address suspicious activity on the network that could lead to potential threats like data breaches.</p>
      <p>and control over devices accessing their corporate network so they can quickly identify and address suspicious activity on the network that could lead to potential threats like data breaches.</p>
      <p>Our technology helps organizations gain comprehensive visibility into and control over devices accessing their corporate network so they can quickly identify and address suspicious activity on the network that could lead to potential threats like data breaches. Our technology helps organizations gain comp</p>
    </section>

    <div class="footer-rule"></div>
    <div class="footer-copyright">©2015 Tallow Crest Software</div>
    <div class="footer-brand">
      <span class="brand-dot"></span>
      <span class="brand-name">Tallow Crest<br>Software</span>
    </div>
  </main>
</body>
</html>
```